Cd Cover design for Chicago based record label.

Cd Cover design for a new single! Song is dedicated to exotic dancers. We do not want our artist pictures on this one. So please use your imagination. Song Title: "Slow Burnout". Thanks? Artist: Lenny Sparrows feat. Kid Tango.

```html
<!DOCTYPE html>
<html lang="en">
<head>
<meta charset="utf-8">
<title>Slow Burnout – Lenny Sparrows feat. Kid Tango</title>
<link rel="stylesheet" href="https://fonts.googleapis.com/css2?family=Anton&family=Big+Shoulders+Stencil+Display:wght@800&family=Oswald:wght@300;400&display=swap">
<style>
  :root {
    --bg: #000000;
    --ink: #ffffff;
    --outline: #000000;
    --gold-light: #e0b25c;
    --gold: #c48a2c;
    --gold-dark: #8e6118;
    --skin-light: #6e5a52;
    --skin-mid: #3a2f2b;
    --stage-dark: #121212;
    --pole-dark: #2c2c2c;
    --pole-light: #a8a8a8;
  }
  html, body {
    margin: 0;
    padding: 0;
    width: 1200px;
    height: 1200px;
    overflow: hidden;
    background: var(--bg);
  }
  .cover {
    position: relative;
    width: 1200px;
    height: 1200px;
    background: var(--bg);
    overflow: hidden;
  }
  .stage-photo {
    position: absolute;
    left: 0;
    top: 0;
    width: 640px;
    height: 1200px;
    background:
      radial-gradient(ellipse 150px 230px at 360px 480px, #8a7a72 0%, rgba(138,122,114,0) 100%),
      radial-gradient(ellipse 110px 420px at 300px 760px, var(--skin-light) 0%, rgba(110,90,82,0) 100%),
      radial-gradient(ellipse 300px 560px at 320px 560px, var(--skin-mid) 0%, var(--stage-dark) 60%, var(--bg) 100%);
  }
  .pole {
    position: absolute;
    left: 462px;
    top: 0;
    width: 14px;
    height: 1130px;
    background: linear-gradient(90deg, var(--pole-dark) 0%, var(--pole-light) 45%, var(--pole-dark) 100%);
  }
  .type-layer {
    position: absolute;
    left: 0;
    top: 0;
    width: 1200px;
    height: 1200px;
  }
  .title-text {
    font-family: "Anton", sans-serif;
    font-weight: 400;
  }
  .title-ring {
    fill: var(--ink);
    stroke: var(--ink);
    stroke-width: 16px;
    stroke-linejoin: round;
  }
  .title-face {
    fill: var(--ink);
    stroke: var(--outline);
    stroke-width: 6px;
    stroke-linejoin: round;
  }
  .artist {
    font-family: "Big Shoulders Stencil Display", sans-serif;
    font-weight: 800;
    fill: url(#gold-fill);
  }
  .featuring {
    font-family: "Oswald", sans-serif;
    fill: var(--ink);
  }
  .featuring .feat-label { font-weight: 300; }
  .featuring .guest { font-weight: 400; }
</style>
</head>
<body>
  <main class="cover">
    <div class="stage-photo" role="img" aria-label="Photograph of a dancer in white lingerie posing beside a dance pole under a soft spotlight"></div>
    <div class="pole" aria-hidden="true"></div>

    <svg class="type-layer" viewBox="0 0 1200 1200" width="1200" height="1200">
      <defs>
        <linearGradient id="gold-fill" x1="0" y1="0" x2="0" y2="1">
          <stop offset="0" stop-color="var(--gold-light)"/>
          <stop offset="0.6" stop-color="var(--gold)"/>
          <stop offset="1" stop-color="var(--gold-dark)"/>
        </linearGradient>
      </defs>

      <g class="title-text" aria-hidden="true">
        <text class="title-ring" x="556" y="282" font-size="250" textLength="476" lengthAdjust="spacingAndGlyphs">SLOW</text>
        <text class="title-ring" x="556" y="456" font-size="200" textLength="476" lengthAdjust="spacingAndGlyphs">BURNOUT</text>
      </g>
      <g class="title-text">
        <title>Slow Burnout</title>
        <text class="title-face" x="556" y="282" font-size="250" textLength="476" lengthAdjust="spacingAndGlyphs">SLOW</text>
        <text class="title-face" x="556" y="456" font-size="200" textLength="476" lengthAdjust="spacingAndGlyphs">BURNOUT</text>
      </g>

      <text class="artist" x="498" y="846" font-size="128" textLength="612" lengthAdjust="spacingAndGlyphs">LENNY SPARROWS</text>

      <text class="featuring" x="744" y="912" font-size="44" textLength="362" lengthAdjust="spacingAndGlyphs"><tspan class="feat-label">FEAT</tspan> <tspan class="guest">KID TANGO</tspan></text>
    </svg>
  </main>
</body>
</html>
```